Online travel site needs edgy website design

tripnook is the first Global Business Travel Website that provides the most comprehensive destination information tailored to suit the business traveller.

It is a ‘one click solution’ that offers direct access to all aspects of business travel, including general information on the city, accommodation and transportation options, economic and financial statistics, key business and services contacts, as well as leisure activities, entertainment suggestions, and listings for any personal needs.

Much more than a travel website, tripnook.com eliminates the need to buy multiple travel books or visit scores of websites. Most importantly, it is the only website that will cover such an extensive range of destinations around the world, while also featuring cities where information is really scarce. The user-friendly and consistent format for all destinations will allow the business traveller to easily navigate through more than 100 information pages on any destination.

tripnook will be simple to navigate, intuitive, unique in design, dynamic, and content rich providing a supreme user experience during navigation of the website.

The website will initially be English and is set to expand to more languages in the future.

A beta site with back-end database has been built - and now we need an edgy state of the art graphic design to reskin it.

LOOK & FEEL

Scope
The design of the site should reflect tripnook’s corporate and user centric philosophy with the following elements:

a. tripnook corporate image and branding
b. the promotion of each city destination
c. tripnook being the starting point of travel, while also a partner during travel
d. the subtle but powerful presence of advertising and sponsorship

All the above must derive from the design outline and elements that are going to be used.

Design Guidelines

Innovative and elegant design, minimalism, simplicity that permits the offering of the required information to be delivered in line with the values of Trust, Care, Discovery & Connection.

In addition:

1. The usability, navigation and the informative character of the corporate web site should not be compromised by the design.
2. The over-segmented pages and over-crowded content per page should be avoided.
3. The design should not only guide the user in an inviting way to the information required but also to intrigue them for further navigation.
4. Advertising space should be anticipated in line with the design character and OMR standard ad sizes.
5. The use of photos / videos should also encouraged.

Key Elements

a. Branding/Logos
Throughout the website branding should be present as a “guarantee seal” for the content accuracy. Corporate logo should be placed on every page while branding should also characterise any content element and/or tool. Appendix contains the current brand guidelines. Should additional sub-logos be required for specific sections, these should be proposed.

b. Fonts
Provided your experience on the website design you are requested to propose alternative font types and sizes always taken into consideration the inviting and user friendly character that the new website should aspire to. The font type that will be proposed must be user friendly in English typography, but also could support other languages in the future.

Given the fact that the majority of the text in the website contains information and listing, the fonts and text layout should not strain and fatigue the reader.

c. SEO
The design should be friendly towards the search engines.

d. Colours
Colour is considered as an integral part of the brand identity. Tripnook.com corporate colours are orange and grey as per the Attached document reference guide.

Different tonalities of the brand colours, or colours in general, should be proposed and applied, guided always by the above described scope of Look & Feel.

e. Section Headings
As presented above, the site’s section headings (refer Overview of the Site.) The principle is to label the content following users’ needs and mindset. However, the label space should be flexible for changes. The labels should facilitate the user to understand the content they host. This is important and should be applied especially to informative content.

Another function that Headings should perform is that of promoting the website’s content, especially when this kind of content will make the user spend more time in the website. This category of Headings should be approached in a more creative and attractive way as to intrigue users to check the content hosted.

f. Icons
Icons are considered necessary in order to provide the user extra help to guide them to reach the information they need quick n’ easy. Icons not only contribute actively to the creation of an attractive look & feel but, most importantly, facilitate navigation and speed up the users’ familiarisation with the website too.

Therefore their design should be eye-catching, comprehensive and dynamic, in accordance to the new site’s colour coding and following the latest trends as these were defined by the look & feel of smart phones.

PIXELHIVE BRIEF REQUIREMENTS
Based on the above, please provide at least two (2) approaches for the following pages – this includes colour palette in line with logo, layout, fonts.

Initial submissions can just address Deliverable 1 & 2 to fine tune design before proceeding further.

Please refer sample screenshots separately attached from raw beta site for content – available for Deliverables 2 -6.

(REFER example sites we like for their creativity: http://www.quillark-studio.co.uk/#Background, http://www.pelorafestas.com.br/, http://brambletondesign.co.uk/ )

Deliverable 1: Landing /Home page
- Access log in –
o Free Account or via WorkLattice/Chatterly etc
o Membership Access – Login
- How to use the site
- Allowance for video or animation
- Destination Selection
- Blog & Social media links

Deliverable 2: Destination Landing Page / Template
This is essentially a city guide template to be used for all cities throughout the site.

This page clearly depicts the four information sections
1. General
2. Business
3. Leisure
4. Personal

Also this page should include:
- Business News Feed
- Advertising & Sponsorship Spaces (according to OMR Standards)
- Destination Time, Weather, FX rates (LIVE feeds)
- Tips

Deliverable 3: Follow the above format but show an Internal Content Page – text only with subheadings

Deliverable 4: Follow the above format but show an Internal Content Page – text and photos

Deliverable 5: Follow the above format but show an Internal Content Page – Listing Sections such as Restaurants (this must also include filter categories)

Deliverable 6: Follow the above format but show an Internal Content Page – Top 10 Experiences – this incorporates address and contact details, photo and sub-text

Deliverable 7: The Membership Landing Page which should include:
1. Intro
2. Advertising & Sponsorship Space
3. The four sections
4. Tips Section
Updates

Hi all - just to reiterate that we are open to different approaches in the design.  We only included the existing screen shots of the beta site to provide you with an idea of the content.  We definitely don't want to see anything similar.....we want it to be edgy yet simple and easy to navigate....we want to create an outstanding user experience!  Cheers Tripnook Team

Reason: Dear Designers - We are extending the period as have not had many submissions at all and want to provide more time. If you have already submitted, we will be in touch shortly with feedback. Thanks for your understanding Tripnook Team

Reason: We would like to give everyone more time so we can find the best and most preferred design.

Target Market(s)

TARGET MARKET
tripnook is a consumer focused website, offering a wide-range of easy-to-use and interactive platforms, for informative and commercial purposes, while also providing attractive and innovative advertising real-estate for potential business partners.

The target audience can be segmented as follows:

Primary Target: Professionals travelling on Business

They require up-to-date reliable information prior and during their travel, as well as facilitation to take action. They need an online Personal Assistant.

The personal characteristics of the primary target group are: busy life, tailored solutions, reliable sources, trusting, caring, and spoiled.
 
The website will have a membership option (for a small annual fee) which will provide customized information for their demographic and preferences. Sub target groups will include:
1. Business Men 40 years
3. Business Women 40 years
5. Business People with reduced mobility

Demographic & Travelling Profile of Business Travellers

• 92% of them use the internet as a source of info
• 54% are males, 38 years old
• 80% holds a college/university degree
• 68% is travelling mainly for leisure and annually 6 times per year
• 52% reserve their ticket through the internet
• 66% is travel internationally

Secondary Targets:

Executive PA’s
Executive personal assistants who need to plan their manager’s travel and provide support information for their trip.

Professionals travelling for Leisure and Partners
They have most probably used the website for their business travel, but consider it also useful for their leisure travel. The generic website, will include enough information to cover most of the leisure needs, as well as the requirements of their partners.

Direct Business-to-Business [B2B] Targets
The direct [B2B] targeted audience includes corporations that would like to use a white label solution for their staff, by using all available destinations or a selected number depending on their global network.

Business-to-Business [B2B] Targets
The [B2B] targeted audience is an indirect audience, for which tripnook promotes its services, and a key revenue stream. The B2B audience consists mainly of a diverse range of professional organisations targeting the business traveller (airlines, hotels, travel agencies, tourism authorities, entertainment companies, services, etc.) tripnook will be targeting these organisations to advertise on the site.
 
Desired Response from Target Groups

The desired response from the consumer targets is:
a) Recurrent use of website
b) Share content/experience with friends and social networking sites
c) Interact on the website’s Blog
d) Register for newsletters and offers
e) Subscribe to Membership
f) Be exposed to commercial advertisements on the website
g) Provide feedback (in the future) for services
h) Use (in the future) online services to purchase products and services
Competition

Industry/Entity Type

Travel

Requirements
Must have
• A clean crisp and professional appearance giving a sense of Trust and Reliability.
Should not have
• It should not look like every other run of the mill travel sites - Roomvale.com, Jaunteo etc

```html
<!DOCTYPE html>
<html lang="en">
<head>
<meta charset="utf-8">
<title>tripnook – Business Travel</title>
<link href="https://fonts.googleapis.com/css2?family=Exo+2:wght@600&family=Oswald:wght@600&family=Roboto+Condensed:wght@400;700&display=swap" rel="stylesheet">
<style>
  :root {
    --orange: #f5821f;
    --orange-panel: rgba(242, 138, 38, 0.9);
    --grey: #505050;
    --blue: #0d3f9e;
    --white: #ffffff;
    --ink: #1a1a1a;
    --box-fill: rgba(150, 158, 172, 0.78);
    --box-frame: #0b0b0b;
  }
  * { margin: 0; padding: 0; box-sizing: border-box; }
  html, body { width: 1200px; height: 750px; overflow: hidden; }
  body { position: relative; font-family: "Roboto Condensed", Arial, sans-serif; background: #c9d5e2; }

  .hero-photo {
    position: absolute; inset: 0;
    background:
      linear-gradient(160deg, rgba(0,0,0,0) 0%, rgba(0,0,0,0) 26%, rgba(236,238,240,0.92) 33%, rgba(214,216,218,0.9) 44%, rgba(120,124,118,0.75) 52%, rgba(70,72,66,0.55) 57%, rgba(0,0,0,0) 63%),
      linear-gradient(180deg, #b9c8d8 0%, #d3dbe4 22%, #cfd8e0 40%, #dfe5ea 58%, #8d9bb2 69%, #41568c 77%, #243a78 86%, #14245a 100%);
  }

  .brand {
    position: absolute; left: 53px; top: 43px;
    display: flex; align-items: center; gap: 14px;
    font-family: "Exo 2", sans-serif; font-weight: 600;
    font-size: 58px; line-height: 1; color: var(--orange);
    letter-spacing: -1px;
  }
  .brand-square { width: 62px; height: 62px; background: var(--grey); }

  .search-panel {
    position: absolute; left: 290px; top: 191px; width: 618px; height: 84px;
    background: var(--orange-panel);
  }
  .search-mark {
    position: absolute; left: 30px; top: 8px; width: 50px; height: 50px;
    border-radius: 50%; background: var(--white);
  }
  .search-caption, .language-select {
    position: absolute; top: 63px; font-weight: 700; font-size: 13px; color: var(--white);
  }
  .search-caption { left: 17px; }
  .language-select { right: 15px; }
  .search-input {
    position: absolute; left: 115px; top: 10px; width: 405px; height: 36px;
    background: var(--white); border: 0;
  }
  .search-button {
    position: absolute; left: 529px; top: 10px; width: 75px; height: 36px;
    background: var(--blue); border: 0; display: flex; align-items: center; justify-content: center;
  }

  .how-to {
    position: absolute; left: 291px; top: 512px; width: 438px; height: 209px;
    border: 7px solid var(--box-frame); background: var(--box-fill);
    padding: 8px 18px 0 24px;
  }
  .how-to h2 {
    font-family: "Oswald", sans-serif; font-weight: 600; font-size: 31px; line-height: 1.1;
    color: var(--orange); text-align: center; text-shadow: 0 1px 2px rgba(0,0,0,0.35);
    margin-bottom: 17px;
  }
  .how-to p { font-size: 11.8px; line-height: 22.5px; color: var(--ink); white-space: nowrap; }
  .read-more {
    position: absolute; left: 77px; bottom: 6px;
    font-weight: 700; font-size: 15px; color: var(--white); text-decoration: none;
  }

  .social-links {
    position: absolute; right: 52px; top: 658px;
    display: flex; align-items: center; gap: 18px;
  }
  .social-links a {
    display: flex; align-items: center; gap: 6px;
    color: var(--white); text-decoration: none; font-weight: 700; font-size: 17px;
  }
  .social-dot { width: 12px; height: 12px; border-radius: 50%; background: var(--white); }
</style>
</head>
<body>
  <div class="hero-photo" role="img" aria-label="Passenger jet of Nordwing Air taking off from a runway at dusk"></div>

  <header class="brand">
    <span class="brand-square"></span>
    <span class="brand-name">tripnook</span>
  </header>

  <form class="search-panel">
    <span class="search-mark"></span>
    <span class="search-caption">Find out now.</span>
    <input class="search-input" type="text" aria-label="Search destinations">
    <button class="search-button" type="button" aria-label="Search">
      <svg width="28" height="28" viewBox="0 0 28 28">
        <circle cx="11" cy="11" r="8" fill="rgba(255,255,255,0.25)" stroke="#ffffff" stroke-width="2.5"/>
        <line x1="17" y1="17" x2="25" y2="25" stroke="#ffffff" stroke-width="4" stroke-linecap="round"/>
      </svg>
    </button>
    <span class="language-select">Languages &#9662;</span>
  </form>

  <section class="how-to">
    <h2>How to use Tripnook</h2>
    <p>It is a ‘one click solution’ that offers direct access to all aspects of business travel,<br>
    including general information on the city, accommodation and transportation<br>
    options, economic and financial statistics, key business and services contacts, as<br>
    well as leisure activities, entertainment suggestions, and listings for any personal<br>
    needs.</p>
    <a class="read-more" href="#">READ MORE...</a>
  </section>

  <nav class="social-links">
    <a href="#"><span class="social-dot"></span>Chatterly</a>
    <a href="#"><span class="social-dot"></span>Chirpline</a>
    <a href="#" aria-label="Blog">
      <svg width="40" height="46" viewBox="0 0 40 46">
        <rect x="1" y="1" width="38" height="44" rx="4" fill="#ffffff"/>
        <g stroke="#cfd6e0" stroke-width="2.5">
          <line x1="8" y1="12" x2="32" y2="12"/><line x1="8" y1="19" x2="32" y2="19"/>
          <line x1="8" y1="26" x2="32" y2="26"/><line x1="8" y1="33" x2="26" y2="33"/>
        </g>
      </svg>
    </a>
    <a href="#" aria-label="Feeds">
      <svg width="42" height="46" viewBox="0 0 42 46">
        <path d="M9 19 A12 12 0 0 1 33 19 Z" fill="#ffffff"/>
        <rect x="3" y="22" width="36" height="5" rx="2.5" fill="#ffffff"/>
        <rect x="3" y="30" width="36" height="5" rx="2.5" fill="#ffffff"/>
        <rect x="3" y="38" width="36" height="5" rx="2.5" fill="#ffffff"/>
      </svg>
    </a>
  </nav>
</body>
</html>
```